Seventh Ridge Wine Labels

Seventh Ridge is an ultra-premium, allocation-only Napa Valley wine brand being built with one objective: to become a long-term cult collectible.

This is not a retail wine.
This is not a lifestyle brand.
This is not driven by marketing trends.

Production is intentionally limited. Access is controlled through private membership. Every decision—from vineyard sourcing to packaging—is made with long-term brand equity in mind.
We are looking for a label system that reflects that level of discipline.

Design a cult-level wine label system for Seventh Ridge that communicates rarity, restraint, and authority at a glance.

This is not decorative Napa.
This must feel like it belongs next to Lanternfield, Corvath, Bellwether—and still stand apart.
Brand Positioning
Ultra-premium, allocation-only Napa wine
Private membership model (not retail-driven)
Production capped intentionally (scarcity is real, not marketing)
Designed to become a long-term collectible

Tone:

Controlled
Intentional
Confident
Understated power

If it feels “designed” or “trying”—it’s wrong.

Core Product Structure

You are designing a system, not a single label.

Foundation Wines:

Cabernet Sauvignon (primary SKU)
Signature Blend

Extensions (future / limited):

Limited Edition Blend (art-driven)
Reserve (ultra minimal, elevated version)
Creative Direction (Critical)

We are pursuing cult minimalism with tension.

Think:

Silence > noise
Precision > decoration
Material > graphics

This should feel:

Like it was inevitable, not created
Recognizable from across the room
Memorable after one exposure
Design Constraints

These are non-negotiable:

Bottle: Velmont Astrano (tall, powerful silhouette)
Glass: Deep antique green (near black)
Capsule: Matte black (baseline)
Front must work with:
Direct glass etching (ghost etch) OR
Minimal premium paper label

No loud colors.
No trendy typography.
No illustrative storytelling.

Brand Elements to Use
Primary mark: VII (Roman numeral 9)
Brand name: SEVENTH RIDGE
Vintage (subtle, not dominant)

Optional concept element:

Varietal composition expressed as a refined system (e.g., “85 · 15” or structured numeric expression)
Design Goals

Your design should achieve:

Instant Recognition
Must be identifiable from 10 feet away
Tactile Value
Feels expensive before you touch it
Even better once you do
Aging Power
This must still look relevant in 20 years
System Cohesion
Cabernet and Blend must feel like a family
Not two separate brands
What We Are NOT Looking For

Avoid immediately:

Gold foil overload
Script fonts / calligraphy
Illustrated vineyards / animals / crests
Trendy “modern winery” aesthetics
Busy compositions
Obvious luxury clichés

If it looks like:

A Napa tasting room brand → reject
A startup wine brand → reject
Something you'd see on a grocery shelf → reject
Creative Territories to Explore

Designers should explore distinct directions, not minor variations:

Pure Etch Minimalism
VII only
Extremely subtle, almost invisible
Power through absence
Architectural Typography
Strong, controlled use of SEVENTH RIDGE
Spatial tension, alignment-driven
Symbol + System
VII + numeric composition (85 / 15, etc.)
Feels like a formula, not decoration
Material-Driven Label
Paper, emboss, deboss, letterpress
Texture carries the design

Target Market(s)

Ultra-high-net-worth individuals, collectors, and allocation-driven wine buyers. Men and women 35–65 Entrepreneurs, executives, investors Already purchasing cult Napa wines ($250–$1,000+ per bottle) Psychographics: Value scarcity over availability Prefer private access over retail Buy for status, cellar, and long-term collection Appreciate restraint, not flash If it appeals to mass retail, it’s wrong.

Industry/Entity Type

Luxury Wine / Fine Wine / Ultra-Premium Consumer Goods

Requirements
Must have
• 1. Lanternfield Why it matters: True cult positioning Feels rare, quiet, and collector-driven What to take: Effortless authority Doesn’t try to look expensive—it just is Strong identity without noise What to avoid: Do not replicate illustration or vintage storytelling style 2. Bellwether (Corvath Family) Why it matters: Masterclass in restraint and architectural design What to take: Minimalism with structure Precision typography and spacing Confidence through reduction What to avoid: Don’t make it cold or overly corporate 3. Corvath Estate Why it matters: One of the most iconic luxury wine labels ever What to take: Timelessness Balance of tradition + authority Label presence without excess What to avoid: Avoid classic/heritage clichés (crests, shields, etc.) 4. Tarsel Nine Why it matters: Instantly recognizable globally Clean, iconic silhouette and branding system What to take: Immediate recognition from distance Cohesive system across vintages What to avoid: Don’t go mainstream or overly commercial 5. Silent Heron Why it matters: Pure scarcity-driven brand power What to take: Understated exclusivity Nothing feels added for effect What to avoid: Do not introduce illustration or narrative-driven visuals

```html
<!DOCTYPE html>
<html lang="en">
<head>
<meta charset="utf-8">
<title>Seventh Ridge — Cabernet Sauvignon Label</title>
<link href="https://fonts.googleapis.com/css2?family=Cormorant+Garamond:wght@500&family=Oswald:wght@400&display=swap" rel="stylesheet">
<style>
  :root {
    --backdrop: #d9cdc7;
    --paper: #fafafa;
    --ink: #141414;
  }
  * { margin: 0; padding: 0; box-sizing: border-box; }
  html, body {
    width: 1200px;
    height: 873px;
    overflow: hidden;
    background: var(--backdrop);
  }
  .label {
    position: absolute;
    left: 288px;
    top: 20px;
    width: 623px;
    height: 833px;
    background: var(--paper);
    box-shadow: 0 6px 24px rgba(0,0,0,0.12);
    overflow: hidden;
    color: var(--ink);
  }
  .mark {
    position: absolute;
    left: 0;
    top: 0;
    width: 259px;
    height: 170px;
    display: flex;
    align-items: center;
    padding-left: 26px;
  }
  .mark__name {
    font-family: "Cormorant Garamond", serif;
    font-weight: 500;
    font-size: 120px;
    line-height: 1;
    color: var(--ink);
  }
  .rule {
    position: absolute;
    background: var(--ink);
  }
  .rule--name-top { left: 259px; top: 170px; width: 80px; height: 1px; }
  .rule--name-side { left: 258px; top: 170px; width: 1px; height: 77px; }
  .rule--cross-v { left: 559px; top: 459px; width: 1.5px; height: 374px; }
  .rule--cross-h { left: 337px; top: 637px; width: 286px; height: 1.5px; }
  .brand-name {
    position: absolute;
    left: 280px;
    top: 188px;
    font-family: "Cormorant Garamond", serif;
    font-weight: 500;
    font-size: 31px;
    line-height: 1;
    letter-spacing: 0.3px;
    white-space: nowrap;
  }
  .varietal {
    position: absolute;
    right: 80px;
    top: 588px;
    font-family: "Cormorant Garamond", serif;
    font-weight: 500;
    font-size: 21px;
    line-height: 1;
    letter-spacing: 1.4px;
  }
  .spec {
    position: absolute;
    top: 786px;
    font-family: "Oswald", sans-serif;
    font-weight: 400;
    font-size: 22px;
    line-height: 1;
  }
  .spec small { font-size: 14px; }
  .spec--abv { left: 32px; }
  .spec--volume { right: 81px; }
</style>
</head>
<body>
  <main class="label">
    <div class="mark"><span class="mark__name">VII</span></div>
    <div class="rule rule--name-top"></div>
    <div class="rule rule--name-side"></div>
    <h1 class="brand-name">SEVENTH RIDGE</h1>
    <p class="varietal">cabernet sauvignon</p>
    <div class="rule rule--cross-v"></div>
    <div class="rule rule--cross-h"></div>
    <p class="spec spec--abv">13.5%<small>Alc./Vol.</small></p>
    <p class="spec spec--volume">75 cl</p>
  </main>
</body>
</html>
```